We are a VOIP, hosted pbx, and cloud services provider. Clients are mostly hotels, offices, business etc. needing phone services.

Our Slogan is : "Refreshingly fair pricing & reliably clear calls"

the logo is attached
the address is
4127 Marrow Pkwy, suite 210
Corvale TX 75390

Phone: 000-000-0000
Fax: 000-000-0000
Website: Vopraxen.com

```html
<!DOCTYPE html>
<html lang="en">
<head>
<meta charset="UTF-8">
<title>Vopraxen Business Card</title>
<link href="https://fonts.googleapis.com/css2?family=Barlow:wght@300;400;500;600&display=swap" rel="stylesheet">
<style>
  :root {
    --page-bg: #e9e9e7;
    --card-white: #f3f3f3;
    --ink: #2b2b2b;
    --ink-soft: #4a4a4a;
    --accent-blue: #1f8fd0;
    --accent-red: #d11f2c;
    --pattern-dark: #2a2a2c;
    --band-blue: #1d9ad6;
    --band-text: #ffffff;
  }
  * { box-sizing: border-box; margin: 0; padding: 0; }
  html, body {
    width: 1200px; height: 900px; overflow: hidden;
    background: var(--page-bg);
    font-family: "Barlow", Arial, sans-serif;
  }
  .canvas { position: relative; width: 1200px; height: 900px; }
  .card {
    position: absolute; left: 320px; width: 560px; height: 320px;
    border-radius: 4px;
    box-shadow: 0 8px 22px rgba(0,0,0,0.16);
    overflow: hidden;
  }
  .card-back { top: 90px; }
  .card-back .pattern-fill {
    position: absolute; inset: 0;
    background:
      radial-gradient(circle at 20% 30%, rgba(233,79,139,0.55), transparent 40%),
      radial-gradient(circle at 75% 25%, rgba(240,140,40,0.5), transparent 40%),
      radial-gradient(circle at 40% 80%, rgba(140,190,40,0.5), transparent 40%),
      radial-gradient(circle at 85% 75%, rgba(31,143,208,0.55), transparent 40%),
      var(--pattern-dark);
  }
  .slogan-band {
    position: absolute; left: 0; right: 0; top: 142px; height: 36px;
    background: var(--band-blue);
    display: flex; align-items: center; justify-content: center;
    color: var(--band-text);
    font-weight: 500; font-size: 17px; letter-spacing: 1.2px;
    text-transform: uppercase; white-space: nowrap;
  }
  .card-front { top: 490px; background: var(--card-white); }
  .brand {
    position: absolute; right: 40px; top: 40px;
    display: flex; align-items: center; gap: 10px;
  }
  .brand-dot {
    width: 22px; height: 22px; border-radius: 50%;
    background: var(--accent-blue);
  }
  .brand-name { font-weight: 600; font-size: 28px; color: var(--ink); }
  .holder {
    position: absolute; left: 44px; top: 112px;
    display: flex; align-items: baseline; gap: 10px;
  }
  .holder-name {
    font-weight: 400; font-size: 27px; color: var(--ink); letter-spacing: 0.5px;
  }
  .holder-title { font-weight: 400; font-size: 14px; color: var(--ink-soft); }
  .contact {
    position: absolute; left: 44px; top: 168px;
    font-size: 15px; line-height: 19px; color: var(--ink);
  }
  .contact-label {
    display: inline-block; width: 16px; color: var(--accent-blue); font-weight: 500;
  }
  .address {
    position: absolute; left: 44px; top: 222px;
    font-size: 15px; line-height: 19px; color: var(--ink);
  }
  .website {
    position: absolute; left: 44px; top: 272px;
    font-size: 16px; font-weight: 500; color: var(--accent-red);
  }
</style>
</head>
<body>
<main class="canvas">
  <section class="card card-back">
    <div class="pattern-fill" role="img" aria-label="Decorative pattern of colourful speech bubbles with greetings on a dark background"></div>
    <div class="slogan-band">Refreshingly fair pricing &amp; reliably clear calls</div>
  </section>

  <section class="card card-front">
    <div class="brand">
      <span class="brand-dot"></span>
      <span class="brand-name">Vopraxen</span>
    </div>
    <div class="holder">
      <span class="holder-name">JOHN DOE</span>
      <span class="holder-title">Managing Partner</span>
    </div>
    <div class="contact">
      <div><span class="contact-label">T</span>000-000-0000</div>
      <div><span class="contact-label">F</span>000-000-0000</div>
    </div>
    <div class="address">
      <div>4127 Marrow Pkwy, suite 210,</div>
      <div>Corvale TX 75390</div>
    </div>
    <div class="website">vopraxen.com</div>
  </section>
</main>
</body>
</html>
```